Harbor of Kellvane - Lanternsdag Poster Design

We need a poster (8.5" x 11") for our Lanternsdag Celebration event June 18 - 19, 2016. I've included the Port logo, event logo, content, and some photos to choose from. Not all the photos have to be used, though. Feel free to use, crop and size photos how you see fit. Colors and fonts are also up to you. Looking for a fun design that screams family fun event!

Target Market(s)

Families

Industry/Entity Type

Event

Requirements
Must have
• The event logo, the Port logo, some photos (provided) and the content provided.

```html
<!DOCTYPE html>
<html lang="en">
<head>
<meta charset="utf-8">
<title>Lanternsdag Celebration Poster</title>
<link href="https://fonts.googleapis.com/css2?family=Montserrat:wght@700;800;900&family=Nunito+Sans:wght@400;700;800&display=swap" rel="stylesheet">
<style>
  :root {
    --navy: #272a5e;
    --sky: #6fc7ef;
    --orange: #d3720b;
    --cream: #ece6bd;
    --white: #ffffff;
    --footer-text: #f6e2c8;
  }
  * { margin: 0; padding: 0; box-sizing: border-box; }
  html, body { width: 927px; height: 1200px; overflow: hidden; }
  body { font-family: "Nunito Sans", sans-serif; background: var(--cream); }
  .poster { position: relative; width: 927px; height: 1200px; overflow: hidden; }

  .backdrop {
    position: absolute; inset: 0 0 270px 0;
    background: linear-gradient(160deg, #e6e0ad 0%, var(--cream) 45%, #f1edd2 100%);
  }
  .info-panel {
    position: absolute; left: 52px; top: 300px; width: 341px; height: 630px;
    background: var(--orange); color: var(--white);
    padding: 128px 0 0 32px;
  }
  .day-title { font-family: "Montserrat", sans-serif; font-weight: 800; font-size: 29px; margin: 0 0 14px 2px; }
  .group { margin-bottom: 17px; padding-left: 3px; }
  .group h3 { font-weight: 800; font-size: 18.5px; line-height: 25px; }
  .group li { list-style: none; font-size: 17px; line-height: 22px; letter-spacing: 0.2px; }

  .photo { position: absolute; }
  .photo-fishing { left: 393px; top: 358px; width: 534px; height: 348px; background: linear-gradient(180deg, #c9c7c0 0%, #8d8a7c 45%, #6b6a55 100%); }
  .photo-musician { left: 393px; top: 714px; width: 209px; height: 216px; background: linear-gradient(160deg, #9ea88e 0%, #4d4a43 60%, #2c2b2a 100%); }
  .photo-dancers { left: 610px; top: 714px; width: 317px; height: 216px; background: linear-gradient(180deg, #b7c6cf 0%, #8e8f82 40%, #6c5a6a 100%); }

  .banner { position: absolute; left: 0; top: 0; width: 927px; height: 400px; }
  .banner-line {
    position: absolute; white-space: nowrap; line-height: 1;
    font-family: "Montserrat", sans-serif;
    transform: translate(-50%, -50%) rotate(-5.8deg);
  }
  .banner-date { left: 466px; top: 150px; color: var(--white); font-weight: 800; font-size: 27px; }
  .banner-title { color: var(--sky); font-weight: 900; font-size: 94px; letter-spacing: 1px; }
  .title-top { left: 472px; top: 210px; }
  .title-bottom { left: 490px; top: 286px; font-size: 90px; }

  .day-two {
    position: absolute; left: 0; top: 930px; width: 927px; height: 160px;
    background: var(--navy); color: var(--white);
  }
  .mark-box {
    position: absolute; background: var(--white);
    display: flex; flex-direction: column; align-items: center; justify-content: center; gap: 8px;
    font-family: "Montserrat", sans-serif; font-weight: 800; color: var(--navy); text-align: center;
  }
  .mark-box .dot { width: 34px; height: 34px; border-radius: 50%; background: var(--sky); }
  .mark-event { left: 55px; top: 14px; width: 149px; height: 134px; font-size: 17px; }
  .mark-port { left: 735px; top: 16px; width: 167px; height: 128px; font-size: 15px; line-height: 18px; }
  .day-two-copy { position: absolute; left: 210px; top: 28px; width: 520px; text-align: center; }
  .day-two-copy h2 { font-family: "Montserrat", sans-serif; font-weight: 800; font-size: 29px; line-height: 34px; }
  .day-two-copy p { font-size: 16.5px; line-height: 22px; }

  .contact {
    position: absolute; left: 0; top: 1090px; width: 927px; height: 110px;
    background: var(--orange); color: var(--footer-text);
    text-align: center; font-size: 20px; line-height: 29px; padding-top: 23px;
  }
  .contact strong { font-weight: 800; }
</style>
</head>
<body>
<main class="poster">
  <div class="backdrop" role="img" aria-label="Faded photo of a white festival tent in the sun"></div>

  <section class="info-panel">
    <h2 class="day-title">On June 18th</h2>
    <div class="group">
      <h3>Fun for the whole family:</h3>
      <ul><li>2-for-1 Moorage</li><li>Live Music</li><li>Hot Dog Vendor</li><li>Power Squadron</li></ul>
    </div>
    <div class="group">
      <h3>Kid’s Activities:</h3>
      <ul><li>Fishing Derby</li><li>Touch a Fire Truck</li><li>Toy Boat Building</li></ul>
    </div>
    <div class="group">
      <h3>Traditional Norwegian<br>Activities:</h3>
      <ul><li>Raising the Mai “Green” Stang</li><li>Traditional Norwegian Food</li><li>and Dancing</li><li>Bonfire Lighting with the Kellvane</li><li>Vikings</li></ul>
    </div>
  </section>

  <div class="photo photo-fishing" role="img" aria-label="Families gathered around a fishing derby tank under a white tent"></div>
  <div class="photo photo-musician" role="img" aria-label="Musician playing acoustic guitar outdoors"></div>
  <div class="photo photo-dancers" role="img" aria-label="Dancers in traditional Norwegian costume by the marina"></div>

  <svg class="banner" viewBox="0 0 927 400" aria-hidden="true">
    <polygon points="0,152 927,56 927,308 0,398" fill="var(--navy)"/>
  </svg>
  <header>
    <p class="banner-line banner-date">June 18 -19 At the Kellvane Marina</p>
    <h1>
      <span class="banner-line banner-title title-top">LANTERNSDAG</span>
      <span class="banner-line banner-title title-bottom">CELEBRATION</span>
    </h1>
  </header>

  <section class="day-two">
    <div class="mark-box mark-event"><span class="dot"></span>Lanternsdag</div>
    <div class="day-two-copy">
      <h2>On June 19th</h2>
      <p>Brindlewater Trails Festival – Keys to Keelport Fun Paddle</p>
      <p>A fun event for paddlers of all levels!</p>
    </div>
    <div class="mark-box mark-port"><span class="dot"></span>Harbor of<br>Kellvane</div>
  </section>

  <footer class="contact">
    <p>For more information, <strong>please call (555) 014-2270 ext. 1</strong></p>
    <p>On the web at <strong>www.harborofkellvane.com/lanternsdag-2</strong></p>
  </footer>
</main>
</body>
</html>
```